GOLD GUTSCHEIN
Zielgruppe
Zielgruppe sind Klienten ab 18 Jahren bis 60. Konzentration soll auf die Schicht zwischen 25 und 35 in der gehobenen Mittelschicht gelegt werden.
Im Vordergrund steht unser FlagShip Produkt ein Gold Ansparplan von der Firma ORU Infos auf www.quillbarrow.com
Es werden allerdings auch auch Vermögensberatung, Versicherungsberatung und Finanzierungsberatung zusätzlich angeboten.Produkt!
Aufgabenstellung
Gestaltungsvorlage für den Reisegutschein
in Form von einen Goldbarren

```html
<!DOCTYPE html>
<html lang="de">
<head>
<meta charset="utf-8">
<title>Reisegutschein</title>
<link href="https://fonts.googleapis.com/css2?family=Saira+Condensed:wght@500;700&family=Titillium+Web:wght@400;600&display=swap" rel="stylesheet">
<style>
:root{
  --page:#ffffff;
  --ink:#121212;
  --ink-soft:#1c1c1c;
  --gold:#f2c34a;
  --gold-light:#fbe39a;
  --gold-deep:#a9761a;
  --yellow:#ffd21c;
  --white:#f4f4f4;
  --silver:#e6e6e6;
}
*{box-sizing:border-box;margin:0;padding:0}
html,body{width:1200px;height:706px;overflow:hidden;background:var(--page)}
body{font-family:"Titillium Web",sans-serif;position:relative}
.voucher{position:absolute;left:250px;width:700px;height:333px;background:radial-gradient(ellipse at 50% 40%,var(--ink-soft),var(--ink) 75%);overflow:hidden}
.voucher--front{top:8px}
.voucher--back{top:365px}

/* front */
.front__title{position:absolute;left:30px;top:42px;font-family:"Saira Condensed",sans-serif;font-weight:700;font-size:68px;line-height:1;letter-spacing:3px;white-space:nowrap;
  background:linear-gradient(180deg,var(--gold-light) 10%,var(--gold) 50%,var(--gold-deep) 95%);-webkit-background-clip:text;background-clip:text;color:transparent}
.brand{position:absolute;left:504px;top:54px;display:flex;align-items:center;gap:8px}
.brand__mark{width:38px;height:38px;border:2px solid var(--gold);background:transparent}
.brand__name{font-family:"Saira Condensed",sans-serif;font-weight:500;font-size:24px;line-height:1;color:var(--gold);white-space:nowrap}
.front__rule{position:absolute;left:0;right:0;top:132px;height:10px;background:linear-gradient(180deg,var(--gold-light),var(--gold-deep))}
.front__photo{position:absolute;left:13px;right:13px;top:142px;height:177px;
  background:linear-gradient(110deg,#5a3a08 0%,#d9a33a 18%,#fbe08a 28%,#b57f1e 40%,#f4cf6a 55%,#8a5c10 70%,#e8b84c 85%,#5a3a08 100%)}
.field{position:absolute;left:38px;height:28px;border-radius:3px;background:linear-gradient(180deg,#fafafa,#d8d8d8);color:var(--ink);display:flex;align-items:center;padding-left:10px;font-family:"Saira Condensed",sans-serif;white-space:nowrap}
.field--number{top:219px;width:213px;font-size:19px}
.field--valid{top:265px;width:172px;font-size:15px}
.field b{font-weight:700;font-size:12px;margin-right:6px}
.price{position:absolute;left:428px;top:146px;width:233px;height:150px;
  background:linear-gradient(160deg,var(--gold-light),var(--gold) 45%,var(--gold-deep));
  clip-path:polygon(0 0,100% 0,100% 88%,95% 94%,90% 88%,85% 94%,80% 88%,75% 94%,70% 88%,65% 94%,60% 88%,55% 94%,50% 88%,45% 94%,40% 88%,35% 94%,30% 88%,25% 94%,20% 88%,15% 94%,10% 88%,5% 94%,0 88%)}
.price__amount{position:absolute;left:0;right:0;top:14px;text-align:center;font-family:"Saira Condensed",sans-serif;font-weight:700;font-size:74px;line-height:1;color:var(--ink);white-space:nowrap}
.price__words{position:absolute;left:0;right:0;top:106px;text-align:center;font-family:"Saira Condensed",sans-serif;font-weight:700;font-size:13.5px;line-height:1;color:var(--ink);white-space:nowrap}

/* back */
.back__tab{position:absolute;left:0;top:0;width:178px;height:38px;background:linear-gradient(180deg,var(--gold-light),var(--gold) 60%,var(--gold-deep))}
.back__tab span{position:absolute;left:13px;bottom:1px;font-family:"Saira Condensed",sans-serif;font-weight:500;font-size:22px;color:var(--ink);line-height:1;white-space:nowrap}
.back__intro{position:absolute;left:184px;top:21px;font-size:11.5px;line-height:14px;color:var(--white);white-space:nowrap}
.back__text{position:absolute;left:13px;top:40px;width:674px;font-size:9.4px;line-height:10.2px;color:var(--white);text-align:justify}
.back__text p{margin-bottom:4px}
.back__gap{float:right;width:208px;height:152px}
.hl{color:var(--yellow)}
.hotlines{position:absolute;left:481px;top:0;width:206px;height:192px;padding:14px 12px 0;color:var(--ink);
  background:linear-gradient(150deg,var(--gold-light),var(--gold) 45%,var(--gold-deep));
  clip-path:polygon(0 0,100% 0,100% 93%,95% 97%,90% 93%,85% 97%,80% 93%,75% 97%,70% 93%,65% 97%,60% 93%,55% 97%,50% 93%,45% 97%,40% 93%,35% 97%,30% 93%,25% 97%,20% 93%,15% 97%,10% 93%,5% 97%,0 93%)}
.hotlines h2{font-family:"Saira Condensed",sans-serif;font-weight:500;font-size:18px;line-height:1;padding-bottom:3px;border-bottom:1.5px solid var(--ink);margin-bottom:5px}
.hotlines p{font-size:9.4px;line-height:10.8px;margin-bottom:5px}
.hotlines strong{font-weight:600}
.hotlines__web{display:block;background:var(--ink);color:var(--yellow);border-radius:3px;font-size:9.6px;padding:1px 6px;width:162px;margin-bottom:4px}
.back__valid{position:absolute;left:13px;top:307px;width:176px;height:20px;border-radius:3px;background:linear-gradient(180deg,#fafafa,var(--silver));font-size:10px;color:var(--ink);padding-left:6px;line-height:20px}
</style>
</head>
<body>

<section class="voucher voucher--front">
  <h1 class="front__title">REISEGUTSCHEIN</h1>
  <div class="brand"><span class="brand__mark"></span><span class="brand__name">ORU TRADING</span></div>
  <div class="front__rule"></div>
  <div class="front__photo" role="img" aria-label="Reihe glänzender Feingold-Barren"></div>
  <div class="field field--number"><b>Nº:</b>0154 5698 5874 121</div>
  <div class="field field--valid"><b>GÜLTIG BIS:</b>10/12/15</div>
  <div class="price">
    <div class="price__amount">€ 100,-</div>
    <div class="price__words">Betrag in Worten: Euro einhundert</div>
  </div>
</section>

<section class="voucher voucher--back">
  <div class="back__tab"><span>REISEGUTSCHEIN</span></div>
  <div class="back__intro">Dieser Reisegutschein ist einlösbar auf Buchungen von:</div>
  <div class="hotlines">
    <h2>BUCHUNGS-HOTLINES</h2>
    <p><strong>Pauschalreise-Katalogangebote</strong><br>+43 / (0) 1234 / 56 789 310<br>office@corvellareisen.com</p>
    <p><strong>Kurzurlaubspackages und Hotelangebote</strong><br>+43 / (0) 1234 / 56 789 302<br>office@corvella-kurzurlaub.com</p>
    <span class="hotlines__web">www.corvellareisen.com</span>
    <p><strong>Gutscheinaussteller:</strong><br>Corvella Marketing GmbH<br>Lindenweg 14, A-4600 Talheim<br>FN 204918k, Firmenbuch LG Talheim</p>
  </div>
  <div class="back__text">
    <div class="back__gap"></div>
    <p><span class="hl">• KURZURLAUBSPACKAGES UND HOTELANGEBOTEN DER CORVELLA PARTNERHOTELS</span><br>
    Ob Sommerurlaub, Winterurlaub, Wellnessurlaub oder Erlebnisurlaub – machen Sie Urlaub wie es Ihnen gefällt! Die aktuellen Angebote finden Sie im Internet auf <span class="hl">www.corvellareisen.com</span>. Die max. Einlösehöhe ist beim jeweiligen Angebot beschrieben. Ebenso informiert Sie die Corvella Kundenservice- und Reservierungszentrale über alle Angebote.</p>
    <p class="hl">DIE BUCHUNG UND EINLÖSUNG DER KURZURLAUBSPACKAGES UND HOTELANGEBOTE IST AUSSCHLIESSLICH ÜBER DIE CORVELLA KUNDENSERVICE – UND RESERVIERUNGSZENTRALE MÖGLICH UND KANN NICHT DIREKT IM HOTEL DURCHGEFÜHRT WERDEN.</p>
    <p><span class="hl">• PAUSCHALREISE-KATALOGANGEBOTEN DER GÄNGIGEN REISEVERANSTALTER</span><br>
    (ausgenommen Sonderangebote)<br>
    Der Reisegutschein ist für alle Flugpauschalreisen und Kreuzfahrten aus Katalogen der gängigen Reiseveranstalter mit einer Reisedauer ab einer Woche unabhängig der Höhe des gebuchten Reisepreises einlösbar. Pro Reisebuchung kann nur ein Reisegutschein eingelöst werden. Die Einlösung des Reisegutscheines ist nicht mit anderen Marketing- und Promotionaktionen kombinierbar. Eine Anrechnung auf bereits bestehende Buchungen ist nicht möglich. Pauschalreise-Katalogangebote sind von Reiseveranstaltern in den Katalogen dargestellte Urlaubsangebote inkl. Flug, Hotelaufenthalt und sonstigen Leistungen. Einzelleistungen (wie zB nur Flug, nur Hotel mit Verpflegung) sind keine Pauschalreise-Katalogangebote.</p>
    <p class="hl">Die Buchung und Einlösung erfolgt telefonisch unter der nebenstehenden Buchungs-Hotline beim jeweils aktuellen Reisebüropartner der Corvella Marketing GmbH.</p>
    <p>Die Buchung gemeinsam reisender Personen (Familie) gilt als eine Buchung, für die die marktübliche Buchungsgebühr verrechnet wird. Der Reisegutschein kann nicht in bar abgelöst werden. Die Einlösung erfolgt gemäß den Gültigkeitsbestimmungen auf <span class="hl">www.corvellareisen.com</span>.</p>
    <p>Dieser Reisegutschein wurde als Incentive bzw. im Rahmen einer Marketingaktion von Firmenname einsetzen als Geschenk ausgegeben und ist nur befristet zur Einlösung gültig. Der Reisegutschein darf vom Empfänger des Geschenks nicht weiterverkauft werden.</p>
  </div>
  <div class="back__valid">Gültig bis ............</div>
</section>

</body>
</html>
```